Flyer für Beratung rund um den Computer
Zielgruppe
Hauptsächlich: Beratung rund um den Computer, individuelle Schulungen, technische Hilfe . Aber auch: Einführung in die Programmierung, Webseitenerstellung etc. Zielgruppe sind Privatpersonen, gerne auch ältere Personen, alle die sich unsicher im Umgang mit Computern fühlen und freundliche, geduldige Hilfe suchen.
Aufgabenstellung
Da meine Zielgruppe eher keine Computerfreaks sind, sollte der Flyer nicht zu technisch aussehen, sondern für Hilfesuchende ansprechend und freundlich wirken.

```html
<!DOCTYPE html>
<html lang="de">
<head>
<meta charset="utf-8">
<title>Flyer – Beratung rund um den Computer</title>
<link rel="stylesheet" href="https://fonts.googleapis.com/css2?family=Anton&family=Poppins:wght@400;600;700&display=swap">
<style>
  :root{
    --navy:#1f3272;
    --blue:#0a84c8;
    --ink:#1c1c1c;
    --white:#ffffff;
    --stage:#ecebe8;
    --photo-warm-a:#b9a79a;
    --photo-warm-b:#e4ddd6;
    --photo-grey-a:#d6d8db;
    --photo-grey-b:#f3f3f3;
    --photo-desk-a:#3a3f45;
    --photo-desk-b:#a8876a;
  }
  *{box-sizing:border-box;margin:0;padding:0}
  html,body{width:1200px;height:1117px;overflow:hidden;background:var(--stage)}
  body{font-family:"Poppins",sans-serif;color:var(--ink)}
  .flyer{position:absolute;left:267px;top:86px;width:667px;height:945px;background:var(--white);overflow:hidden;box-shadow:0 4px 18px rgba(0,0,0,.15)}
  .abs{position:absolute}
  .hero-backdrop{left:0;top:0;width:667px;height:252px;background:linear-gradient(135deg,var(--photo-grey-b),var(--photo-grey-a))}
  .hero-photo{left:0;top:0;width:270px;height:230px;background:linear-gradient(120deg,var(--photo-warm-a),var(--photo-warm-b));clip-path:polygon(0 0,246px 0,270px 115px,258px 230px,0 230px)}
  .hero-shapes{left:0;top:0}
  .headline{left:358px;top:52px;font-family:"Anton",sans-serif;font-weight:400;font-size:50px;line-height:51px;color:var(--navy)}
  .headline .accent{color:var(--blue)}
  .intro{left:64px;top:272px;width:540px;text-align:center;font-size:11.2px;line-height:15.3px}
  .banner{left:55px;top:346px;width:558px;height:31px}
  .banner span{position:absolute;inset:0;display:flex;align-items:center;justify-content:center;color:var(--white);font-weight:700;font-size:13px}
  .desk-photo{left:285px;top:566px;width:382px;height:248px;background:linear-gradient(140deg,var(--photo-desk-a),var(--photo-desk-b));clip-path:polygon(36px 0,100% 0,100% 100%,36px 100%,0 124px)}
  .info-panel{left:34px;top:460px;width:600px;height:137px;background:var(--navy);border-radius:14px}
  .question-box{left:68px;top:390px;width:531px;height:112px;background:var(--white);border-left:2px solid var(--navy);border-right:2px solid var(--navy);border-radius:0 0 12px 12px}
  .questions{left:92px;top:387px;width:500px;list-style:none;font-size:10.6px;line-height:13px}
  .questions li{position:relative;padding-left:18px;margin-bottom:12.5px}
  .questions li svg{position:absolute;left:0;top:2px}
  .callout{left:68px;top:473px;width:531px;text-align:center;color:var(--blue);font-weight:700;font-size:11px;line-height:14px}
  .panel-text{left:63px;top:512px;width:400px;color:var(--white);font-weight:600;font-size:11.4px;line-height:14.3px}
  .badge{left:470px;top:521px;width:102px;height:102px;border-radius:50%;background:var(--navy);display:flex;align-items:center;justify-content:center;text-align:center;color:var(--white);font-weight:600;font-size:12px;line-height:15px}
  .services{left:55px;width:230px}
  .services h3{color:var(--blue);font-weight:700;font-size:12.8px;line-height:16px;margin-bottom:2px}
  .services ul{list-style:none;font-size:11px;line-height:14.8px}
  .services li{position:relative;padding-left:17px}
  .services li svg{position:absolute;left:0;top:3px}
  .cols{display:flex;gap:18px}
  .contact{left:0;top:0}
  .contact-text{left:338px;top:843px;color:var(--white)}
  .phone{display:flex;align-items:center;gap:9px;font-weight:700;font-size:33px;line-height:38px}
  .line{display:flex;align-items:center;gap:10px;font-weight:600;font-size:11.5px;line-height:15px;margin-top:4px;padding-left:9px}
</style>
</head>
<body>
<main class="flyer">
  <div class="abs hero-backdrop" role="img" aria-label="Aufgehellter Schreibtisch mit Laptop, Pflanze und Kaffeetasse"></div>
  <svg class="abs hero-shapes" width="667" height="340" viewBox="0 0 667 340">
    <polygon points="0,230 258,230 270,115 246,0 259,0 332,125 286,252 0,252" fill="var(--navy)"/>
    <polygon points="246,0 259,0 320,125 276,240 262,240 306,125" fill="var(--blue)"/>
    <polygon points="0,252 53,252 0,333" fill="var(--navy)"/>
  </svg>
  <div class="abs hero-photo" role="img" aria-label="Foto: Paar sitzt lächelnd gemeinsam vor einem Laptop in der Küche"></div>
  <h1 class="abs headline">Computer -<br>Alles, Nur Kein<br><span class="accent">Hexenwissen</span></h1>

  <p class="abs intro">Ganz egal, was Sie im Zusammenhang mit Ihrem Rechner umtreibt - ob Sie sich manchmal einfach etwas unsicher fühlen, mit einer Anwendung nicht zurecht kommen oder Ihr Rechner nicht so reagiert, wie er sollte - mein Ziel ist es, dass Sie sich im Umgang mit Ihrem Computer sicher fühlen und Freude daran haben.</p>

  <div class="abs banner">
    <svg width="558" height="31" viewBox="0 0 558 31"><polygon points="12,0 546,0 558,15.5 546,31 12,31 0,15.5" fill="var(--blue)"/></svg>
    <span>Auch viele andere Themen werfen immer wieder Fragen auf:</span>
  </div>

  <div class="abs desk-photo" role="img" aria-label="Foto: Laptop, Website-Skizze auf Papier, Smartphone in der Hand und Cappuccino auf Holztisch"></div>
  <div class="abs info-panel"></div>
  <div class="abs question-box"></div>
  <ul class="abs questions">
    <li><svg width="11" height="9" viewBox="0 0 12 10"><path d="M1 5l3.5 3.5L11 1.5" stroke="var(--blue)" stroke-width="2.6" fill="none"/></svg>Ich brauche einen neuen Rechner - wie finde ich heraus, was ich wirklich brauche?</li>
    <li><svg width="11" height="9" viewBox="0 0 12 10"><path d="M1 5l3.5 3.5L11 1.5" stroke="var(--blue)" stroke-width="2.6" fill="none"/></svg>Wie organisiere ich meinen Rechner damit ich alles schnell wiederfinde?</li>
    <li><svg width="11" height="9" viewBox="0 0 12 10"><path d="M1 5l3.5 3.5L11 1.5" stroke="var(--blue)" stroke-width="2.6" fill="none"/></svg>Wie bekomme ich die Fotos von meiner Kamera / meinem Smartphone auf meinen Rechner? ,und so weiter.</li>
  </ul>
  <p class="abs callout">Legen Sie los - egal wie klein oder groß Ihre Frage ist - ich helfe gerne!</p>
  <p class="abs panel-text">Und für alle, die etwas mehr wissen wollen - z.B. wie das mit dem Programmieren eigentlich funktioniert, wie eine Webseite entsteht, wofür ein Router benötigt wird, wie nutze ich eine KI, usw. - ich gebe gerne eine Einführung dazu.</p>
  <div class="abs badge">Rechner<br>ganz leicht</div>

  <section class="abs services" style="top:626px">
    <h3>Beratung rund um Ihren Rechner:</h3>
    <div class="cols">
      <ul>
        <li><svg width="10" height="8" viewBox="0 0 11 9"><path d="M1 4.5l3 3L10 1" stroke="var(--ink)" stroke-width="2.4" fill="none"/></svg>Kauf</li>
        <li><svg width="10" height="8" viewBox="0 0 11 9"><path d="M1 4.5l3 3L10 1" stroke="var(--ink)" stroke-width="2.4" fill="none"/></svg>Organisation</li>
        <li><svg width="10" height="8" viewBox="0 0 11 9"><path d="M1 4.5l3 3L10 1" stroke="var(--ink)" stroke-width="2.4" fill="none"/></svg>Anwendungen</li>
        <li><svg width="10" height="8" viewBox="0 0 11 9"><path d="M1 4.5l3 3L10 1" stroke="var(--ink)" stroke-width="2.4" fill="none"/></svg>Optimierung</li>
      </ul>
      <ul>
        <li><svg width="10" height="8" viewBox="0 0 11 9"><path d="M1 4.5l3 3L10 1" stroke="var(--ink)" stroke-width="2.4" fill="none"/></svg>Internet</li>
        <li><svg width="10" height="8" viewBox="0 0 11 9"><path d="M1 4.5l3 3L10 1" stroke="var(--ink)" stroke-width="2.4" fill="none"/></svg>Datensicherung</li>
        <li><svg width="10" height="8" viewBox="0 0 11 9"><path d="M1 4.5l3 3L10 1" stroke="var(--ink)" stroke-width="2.4" fill="none"/></svg>und vieles mehr</li>
      </ul>
    </div>
  </section>

  <section class="abs services" style="top:722px">
    <h3>Für alle, die mehr wollen:</h3>
    <ul>
      <li><svg width="10" height="8" viewBox="0 0 11 9"><path d="M1 4.5l3 3L10 1" stroke="var(--ink)" stroke-width="2.4" fill="none"/></svg>Einführung in die Programmierung</li>
      <li><svg width="10" height="8" viewBox="0 0 11 9"><path d="M1 4.5l3 3L10 1" stroke="var(--ink)" stroke-width="2.4" fill="none"/></svg>Erstellen einer Website</li>
      <li><svg width="10" height="8" viewBox="0 0 11 9"><path d="M1 4.5l3 3L10 1" stroke="var(--ink)" stroke-width="2.4" fill="none"/></svg>Wie komme ich einer KI näher?</li>
      <li><svg width="10" height="8" viewBox="0 0 11 9"><path d="M1 4.5l3 3L10 1" stroke="var(--ink)" stroke-width="2.4" fill="none"/></svg>oder: was interessiert Sie?</li>
    </ul>
  </section>

  <section class="abs services" style="top:817px">
    <h3>Technische Hilfe:</h3>
    <ul>
      <li><svg width="10" height="8" viewBox="0 0 11 9"><path d="M1 4.5l3 3L10 1" stroke="var(--ink)" stroke-width="2.4" fill="none"/></svg>Anschluß von Peripheriegeräten</li>
      <li><svg width="10" height="8" viewBox="0 0 11 9"><path d="M1 4.5l3 3L10 1" stroke="var(--ink)" stroke-width="2.4" fill="none"/></svg>Einbinden von Peripheriegeräten ins Netzwerk / WLAN</li>
      <li><svg width="10" height="8" viewBox="0 0 11 9"><path d="M1 4.5l3 3L10 1" stroke="var(--ink)" stroke-width="2.4" fill="none"/></svg>Kleinere Reparaturen</li>
      <li><svg width="10" height="8" viewBox="0 0 11 9"><path d="M1 4.5l3 3L10 1" stroke="var(--ink)" stroke-width="2.4" fill="none"/></svg>oder: was brauchen Sie?</li>
    </ul>
  </section>

  <svg class="abs contact" width="667" height="945" viewBox="0 0 667 945">
    <polygon points="322,823 667,823 667,945 0,945 0,925 285,925" fill="var(--blue)"/>
  </svg>
  <div class="abs contact-text">
    <div class="phone">
      <svg width="28" height="28" viewBox="0 0 32 32"><circle cx="16" cy="16" r="16" fill="var(--white)"/><path d="M11 8.5l3 .2 1.4 4-2 1.6c1 2.2 2.4 3.6 4.4 4.5l1.6-2 4 1.4.2 3c-.8 1.6-2.4 2.3-4 2-5.6-1.1-9.5-5-10.6-10.7-.3-1.6.4-3.2 2-4z" fill="var(--blue)"/></svg>
      0160 555 0192
    </div>
    <div class="line"><svg width="13" height="13" viewBox="0 0 14 14"><circle cx="7" cy="7" r="7" fill="var(--white)"/><rect x="3.5" y="4.5" width="7" height="5" fill="none" stroke="var(--blue)" stroke-width="1"/><path d="M3.5 4.5L7 7.3l3.5-2.8" fill="none" stroke="var(--blue)" stroke-width="1"/></svg>hallo@rechner-ganz-leicht.de</div>
    <div class="line"><svg width="13" height="13" viewBox="0 0 14 14"><circle cx="7" cy="7" r="7" fill="var(--white)"/><circle cx="7" cy="7" r="4" fill="none" stroke="var(--blue)" stroke-width="1"/><path d="M3 7h8M7 3c-2 2.5-2 5.5 0 8M7 3c2 2.5 2 5.5 0 8" fill="none" stroke="var(--blue)" stroke-width="1"/></svg>www.rechner-ganz-leicht.de</div>
  </div>
</main>
</body>
</html>
```